Zentrova - Creative Automation

We are a software house for Audio Visual Systems integration/automation and home automation. we develop innovative software to automate a variety of devices mainly related to audio visuals and we design touch panel user interfaces to control these systems.

We would like to see designs that stick to our colours and theme, which you can find on our webpage www.zentrova.com.au

The final design should communicate touch panels, innovation, software and automation.

Industry/Entity Type

Software

Requirements
Must have
• The business card must show the following information:
Name example : Derek Malloway
Qualification example: B Eng ICT(CompSys) Dip EngPrac
Title example : Control Systems Programmer
Mobile Phone, Company phone, Email address ,Company website

```html
<!DOCTYPE html>
<html lang="en">
<head>
<meta charset="utf-8">
<title>Zentrova – Business Card</title>
<link rel="stylesheet" href="https://fonts.googleapis.com/css2?family=Arimo:wght@400;700&display=swap">
<style>
  :root {
    --page-bg: #eceae6;
    --card-outline: #2b2a78;
    --green-deep: #0e6b3a;
    --green-mid: #16873f;
    --green-rim: #45b04a;
    --cyan: #29a9e0;
    --brand-green: #22a35a;
    --brand-blue: #1a6fb8;
    --tagline: #3f4a46;
    --white: #ffffff;
  }
  * { box-sizing: border-box; margin: 0; padding: 0; }
  html, body { width: 1200px; height: 1200px; overflow: hidden; }
  body {
    background: var(--page-bg);
    font-family: "Arimo", Arial, sans-serif;
    position: relative;
  }
  .card {
    position: absolute;
    left: 170px;
    width: 860px;
    height: 470px;
    border: 7px solid var(--card-outline);
    border-radius: 30px;
    overflow: hidden;
  }

  /* Front side */
  .card--front {
    top: 80px;
    background: var(--green-deep);
  }
  .card__texture {
    position: absolute;
    inset: 0;
    background: linear-gradient(90deg, var(--cyan) 0%, #1f8f9c 30%, var(--green-deep) 62%);
  }
  .brand {
    position: absolute;
    right: 70px;
    top: 150px;
    display: flex;
    align-items: center;
    gap: 26px;
  }
  .brand__square {
    width: 90px;
    height: 90px;
    background: var(--brand-blue);
    border-radius: 6px;
  }
  .brand__text { display: flex; flex-direction: column; }
  .brand__name {
    font-size: 104px;
    font-weight: 700;
    color: var(--brand-green);
    letter-spacing: -1px;
    line-height: 1;
  }
  .brand__tagline {
    margin-top: 8px;
    font-size: 22px;
    font-weight: 700;
    color: var(--tagline);
    padding-left: 90px;
  }

  /* Back side */
  .card--back {
    top: 650px;
    background: var(--green-rim);
  }
  .card__face {
    position: absolute;
    inset: 0 22px 0 0;
    border-right: 6px solid var(--card-outline);
    border-radius: 0 24px 24px 0;
    background: linear-gradient(90deg, var(--green-mid), #1a9444);
  }
  .card__face-texture {
    position: absolute;
    inset: 0;
    background: linear-gradient(180deg, rgba(255,255,255,0.04), rgba(0,0,0,0.06));
  }
  .contact {
    position: absolute;
    left: 46px;
    top: 62px;
    width: 390px;
    color: var(--white);
  }
  .contact__name { font-size: 48px; font-weight: 700; line-height: 1; white-space: nowrap; }
  .contact__title { margin: 14px 0 0 28px; font-size: 22px; font-weight: 700; }
  .contact__quals { margin: 4px 0 0 28px; font-size: 20px; font-weight: 700; }
  .contact__company { margin: 92px 0 0 40px; font-size: 34px; font-weight: 700; }
  .contact__lines { list-style: none; margin: 18px 0 0 66px; font-size: 24px; font-weight: 700; line-height: 1.2; }
  .panel {
    position: absolute;
    right: 44px;
    top: 40px;
    width: 330px;
    height: 380px;
    background: var(--white);
    border: 6px solid var(--card-outline);
    border-radius: 28px;
    display: flex;
    align-items: center;
    justify-content: center;
    gap: 16px;
  }
  .panel__square {
    width: 40px;
    height: 40px;
    background: var(--brand-blue);
    border-radius: 4px;
  }
  .panel__name {
    font-size: 50px;
    font-weight: 700;
    color: var(--brand-green);
  }
</style>
</head>
<body>
  <section class="card card--front">
    <div class="card__texture" role="img" aria-label="Circuit-line pattern fading from cyan to green"></div>
    <div class="brand">
      <div class="brand__square"></div>
      <div class="brand__text">
        <span class="brand__name">Zentrova</span>
        <span class="brand__tagline">Creative Automation</span>
      </div>
    </div>
  </section>

  <section class="card card--back">
    <div class="card__face">
      <div class="card__face-texture" role="img" aria-label="Circuit-trace line pattern on green"></div>
      <div class="contact">
        <h1 class="contact__name">Derek Malloway</h1>
        <p class="contact__title">Control Systems Programmer</p>
        <p class="contact__quals">B Eng ICT(CompSys)Dip EngPrac</p>
        <p class="contact__company">Company Name</p>
        <ul class="contact__lines">
          <li>Phone:</li>
          <li>Email:</li>
          <li>Website:</li>
        </ul>
      </div>
      <div class="panel">
        <div class="panel__square"></div>
        <span class="panel__name">Zentrova</span>
      </div>
    </div>
  </section>
</body>
</html>
```